TLW Indianapolis Website

Create a web design to represent our image as an up and coming, technology focused neuropsychological practice.
TLW is short for Bright Harbor Pediatric Collective, we specialize in neuropsychological assessments and intervention in pediatric populations. Directed at a more affluent population, our target market is parents age 25-30+ with children ages 2-22.
We would like a coming soon web page that would allow for email submission to be notified when we are online, as well as provide our contact information for immediate referrals.
Target Market(s)
Parents aged 25+ with children aged 2-22
Industry/Entity Type
Group
Requirements
Must have
- Must provide our contact information as follows:
VoiceLink number: 4089231576 (would be nice to have a VoiceLink direct call button)
Email Address: contact@tlwclinicdemo.com
Our brief summary of what we do:
"At Bright Harbor Pediatric Collective we are committed to providing you with an unsurpassable quality of care. Under the direction of Dr. Rosalind T. Abernathy, one of nine Board Certified Clinical Neuropsychologists in the state of Indiana, TLW has developed a unique approach of utilizing technology to aide in neurobehavioral assessments like nobody else in the business. Our revolutionary utilization of technology as a diagnostic tool, coupled with our traditionally rooted experience and expertise, create the ideal package to insure your child’s future success, both in and out of the classroom."
Nice to have
- Nice to have the ability for patients to fill out a form with basic demographics (name, age, city, email, phone) along with a brief note on services they're seeking on a separate page.
A separate page that contains our consent forms that would be available for download (see attached).

```html
<!DOCTYPE html>
<html lang="en">
<head>
<meta charset="utf-8">
<title>Bright Harbor Pediatric Collective — Coming Soon</title>
<link rel="stylesheet" href="https://fonts.googleapis.com/css2?family=Arimo:wght@400;700&display=swap">
<style>
:root{
  --navy-deep:#0d2a4a;
  --navy:#1b4d80;
  --navy-glow:#4f7ea8;
  --band:#0f3358;
  --band-edge:#2a5e91;
  --ink:#333333;
  --ink-soft:#555555;
  --field-line:#b9b9b9;
  --field-hint:#a8a8a8;
  --panel:#d6d6d6;
  --form-panel:#bdbdbd;
  --lower-bg:#cbcbcb;
  --btn-top:#5a5a5a;
  --btn-bottom:#1e1e1e;
  --voice-blue:#2aa3df;
  --leaf-green:#8cc41a;
}
*{box-sizing:border-box;margin:0;padding:0}
html,body{width:1200px;height:1182px;overflow:hidden}
body{position:relative;font-family:"Arimo",Arial,sans-serif;color:var(--ink);
  background:linear-gradient(180deg,#e2e2e2 443px,#f4f4f4 600px,#ececec 740px,var(--lower-bg) 760px,var(--lower-bg) 100%)}
.abs{position:absolute}

/* header */
.masthead{left:0;top:0;width:1200px;height:443px;
  background:radial-gradient(ellipse 420px 330px at 600px 110px,var(--navy-glow),var(--navy) 60%,#17416c 100%)}
.masthead::before{content:"";position:absolute;left:0;top:0;width:1200px;height:40px;
  background:linear-gradient(180deg,var(--navy-deep),rgba(13,42,74,0))}
.brand-name{left:0;top:150px;width:1200px;text-align:center;font-size:40px;font-weight:400;
  line-height:48px;color:#ffffff}
.summary-band{left:0;top:331px;width:1200px;height:104px;background:var(--band)}
.summary-band p{position:absolute;left:117px;top:4px;width:968px;font-size:12px;line-height:24px;
  color:#fff;text-align:left;text-shadow:0 1px 1px rgba(0,0,0,.6)}
.band-edge{left:0;top:435px;width:1200px;height:8px;background:var(--band-edge)}
.header-shadow{left:110px;top:443px;width:980px;height:22px;
  background:radial-gradient(ellipse 50% 100% at 50% 0,rgba(0,0,0,.28),rgba(0,0,0,0))}

/* announcement */
.announce{left:0;top:481px;width:1200px;text-align:center;font-size:22px;font-weight:700;line-height:26.5px;color:var(--ink)}
.notify-box{left:421px;top:584px;width:356px;height:90px;background:var(--panel);border-radius:4px}
.notify-title{left:0;top:11px;width:356px;text-align:center;font-size:14px;font-weight:700;color:#444}
.field{background:#fff;border:1px solid var(--field-line);border-radius:4px;font-size:11px;color:var(--field-hint);padding:0 11px;display:flex;align-items:center}
.notify-input{left:18px;top:40px;width:245px;height:37px}
.btn{display:flex;align-items:center;justify-content:center;color:#fff;font-weight:700;letter-spacing:1px;
  background:linear-gradient(180deg,var(--btn-top),var(--btn-bottom));border:1px solid #111;border-radius:4px;
  box-shadow:inset 0 1px 0 rgba(255,255,255,.3),0 0 0 2px #9a9a9a}
.notify-btn{left:267px;top:41px;width:72px;height:36px;font-size:12px}

/* contact row */
.contact-item{top:700px;display:flex;align-items:center;gap:8px;font-size:12px;font-weight:700;color:var(--ink);white-space:nowrap}
.divider-shadow{left:120px;top:740px;width:980px;height:16px;
  background:radial-gradient(ellipse 50% 100% at 50% 0,rgba(0,0,0,.3),rgba(0,0,0,0))}

/* faq */
.section-title{font-size:14px;font-weight:700;color:var(--ink)}
.faq-list{left:209px;top:817px;list-style:none}
.faq-list li{position:relative;padding-left:20px;font-size:12px;line-height:14px;height:29px;color:var(--ink)}
.faq-list li::before{content:"";position:absolute;left:1px;top:3px;width:6px;height:6px;border-radius:50%;background:#333}

/* enquiry form */
.form-sub{left:661px;top:796px;font-size:9px;color:var(--ink-soft)}
.enquiry-box{left:661px;top:817px;width:348px;height:324px;background:var(--form-panel);border:1px solid #b0b0b0;border-radius:4px}
.enquiry-box .field{position:absolute;height:32px}
.detail-field{align-items:flex-start !important;padding-top:10px !important}
.send-btn{left:249px;top:276px;width:84px;height:35px;font-size:14px}
</style>
</head>
<body>

<header class="masthead abs">
  <div class="brand-name abs">Bright Harbor Pediatric Collective</div>
</header>

<section class="summary-band abs">
  <p>At Bright Harbor Pediatric Collective we are committed to providing you with an unsurpassable quality of care. Under the direction of Dr. Rosalind T. Abernathy, one of nine Board Certified Clinical Neuropsychologists in the state of Indiana, TLW has developed a unique approach of utilizing technology to aide in neurobehavioral assessments like nobody else in the business. Our revolutionary utilization of technology as a diagnostic tool, coupled with our traditionally rooted experience and expertise, create the ideal package to insure your child’s future success, both in and out of the classroom.</p>
</section>
<div class="band-edge abs"></div>
<div class="header-shadow abs"></div>

<h1 class="announce abs">We are currently building the new site which will be ready soon.<br>In the mean time you can contact us or send to us your concerns and questions.<br>We are happy to serve you</h1>

<form class="notify-box abs">
  <div class="notify-title abs">Be the first one to know when our site goes live</div>
  <div class="field notify-input abs">Enter your email address</div>
  <div class="btn notify-btn abs">SUBMIT</div>
</form>

<div class="contact-item abs" style="left:205px">
  <svg width="30" height="30" viewBox="0 0 30 30"><rect x="1" y="1" width="28" height="28" rx="5" fill="var(--voice-blue)" stroke="#1b7fb3"/><path d="M10 9c1-1 2 0 3 2s0 2-1 3c1 2 2 3 4 4 1-1 1-2 3-1s3 2 2 3c-1 2-3 2-5 1-3-1-6-4-7-7-1-2-1-4 1-5z" fill="#fff"/></svg>
  <span>VoiceLink number: 4089231576</span>
</div>
<div class="contact-item abs" style="left:450px">
  <svg width="32" height="30" viewBox="0 0 32 30"><rect x="1" y="3" width="30" height="24" fill="#fafafa" stroke="#c4c4c4"/><path d="M1 3l15 13L31 3M1 27l11-11M31 27L20 16" fill="none" stroke="#c4c4c4"/></svg>
  <span>Email Address: contact@tlwclinicdemo.com</span>
</div>
<div class="contact-item abs" style="left:781px">
  <svg width="34" height="34" viewBox="0 0 34 34"><path d="M10 1h14v15h9L17 33 1 16h9z" fill="var(--leaf-green)" stroke="#5f9a0c"/></svg>
  <span>Download our consent forms</span>
</div>
<div class="divider-shadow abs"></div>

<h2 class="section-title abs" style="left:209px;top:778px">Frequently Asked Questions</h2>
<ul class="faq-list abs">
  <li>What are your services?</li>
  <li>What is a Pediatric Neurobehavioral Psychological Evaluation?</li>
  <li>When is a Neurobehavioral Psychological Evaluation needed?</li>
  <li>Do you have a specialty?</li>
  <li>How do I make an appointment?</li>
  <li>How long is the wait?</li>
</ul>

<h2 class="section-title abs" style="left:661px;top:778px">Questions and Concerns? Email Us</h2>
<div class="form-sub abs">If you have concerns and questions or anything we can help you</div>
<form class="enquiry-box abs">
  <div class="field" style="left:13px;top:14px;width:320px">Name</div>
  <div class="field" style="left:13px;top:50px;width:320px">Email</div>
  <div class="field" style="left:13px;top:86px;width:320px">Phone Number</div>
  <div class="field" style="left:13px;top:123px;width:153px">Age</div>
  <div class="field" style="left:179px;top:123px;width:154px">City</div>
  <div class="field detail-field" style="left:13px;top:160px;width:320px;height:110px">Details</div>
  <div class="btn send-btn abs">SUBMIT</div>
</form>

</body>
</html>
```